Postcard Mailer

We are a pizza pub that is the only local restaurant that offers and delivers pizza, burgers, salads and wings.

We just opened and want to send out a postcard to the community. thinking on one side a nice design with pics etc. then on the back a list of our daily food and drink specials.

Restaurant

eb1f27

```html
<!DOCTYPE html>
<html lang="en">
<head>
<meta charset="utf-8">
<title>Rosalie and Matteo – Postcard Mailer Back</title>
<link rel="stylesheet" href="https://fonts.googleapis.com/css2?family=Open+Sans:wght@400;600;700&display=swap">
<style>
  :root {
    --brand-red: #eb1f27;
    --ink: #2b2b2b;
    --paper: #ffffff;
    --crust: #c98a4a;
    --cheese: #efdcb4;
    --sauce: #b8503a;
    --wood: #8a5a3a;
  }
  html, body {
    margin: 0;
    padding: 0;
    overflow: hidden;
    background: var(--paper);
  }
  .postcard {
    position: relative;
    width: 1200px;
    height: 930px;
    overflow: hidden;
    background: var(--paper);
    font-family: "Open Sans", sans-serif;
    color: var(--ink);
  }
  .header-photo {
    position: absolute;
    left: 0; top: 0;
    width: 915px; height: 302px;
    background:
      radial-gradient(ellipse at 20% 60%, rgba(184,80,58,.55), transparent 55%),
      radial-gradient(ellipse at 85% 70%, rgba(201,138,74,.7), transparent 50%),
      linear-gradient(135deg, var(--wood) 0%, var(--cheese) 45%, var(--crust) 100%);
  }
  .brand-mark {
    position: absolute;
    left: 0; top: 0;
    width: 263px; height: 302px;
    display: flex;
    flex-direction: column;
    align-items: center;
    justify-content: center;
    gap: 12px;
    color: var(--paper);
    font-weight: 700;
    text-align: center;
  }
  .brand-mark .dot {
    width: 90px; height: 90px;
    border-radius: 50%;
    background: var(--paper);
    opacity: .9;
  }
  .brand-mark .name { font-size: 22px; line-height: 1.15; }
  .brand-mark .place { font-size: 14px; line-height: 1.3; }
  .contact-panel {
    position: absolute;
    left: 263px; top: 0;
    width: 629px; height: 302px;
    background: linear-gradient(to bottom, rgba(255,255,255,1) 0%, rgba(255,255,255,.95) 50%, rgba(255,255,255,.5) 100%);
    color: var(--brand-red);
  }
  .contact-panel .street {
    position: absolute; left: 20px; top: 42px;
    margin: 0; font-size: 24px; font-weight: 700; letter-spacing: .2px;
  }
  .contact-panel .phone {
    position: absolute; left: 20px; top: 76px;
    margin: 0; font-size: 35px; font-weight: 400;
  }
  .contact-panel .web {
    position: absolute; left: 22px; top: 120px;
    margin: 0; font-size: 35px; font-weight: 400;
  }
  .specials {
    position: absolute;
    left: 0; top: 302px;
    width: 588px; height: 474px;
    background:
      linear-gradient(rgba(255,255,255,.72), rgba(255,255,255,.72)),
      radial-gradient(ellipse at 30% 40%, var(--sauce), transparent 60%),
      radial-gradient(ellipse at 75% 65%, var(--crust), transparent 55%),
      linear-gradient(160deg, var(--cheese), var(--wood));
  }
  .special {
    position: absolute;
    font-size: 19px;
    line-height: 26px;
    margin: 0;
  }
  .special .day { display: block; font-weight: 700; margin-bottom: 3px; }
  .special .lead { font-weight: 400; margin-bottom: 0; }
  .col-a { left: 29px; }
  .col-b { left: 319px; }
  .footer-photo {
    position: absolute;
    left: 0; top: 776px;
    width: 152px; height: 154px;
    background: linear-gradient(to right, var(--wood), #b98a67 60%, #d9b89c);
  }
  .mail-label {
    position: absolute;
    font-size: 32px;
    color: #000;
    white-space: nowrap;
  }
  .postage-area { left: 967px; top: 138px; }
  .address-area { left: 795px; top: 496px; }
  .barcode-area { left: 526px; top: 837px; }
</style>
</head>
<body>
<main class="postcard">
  <div class="header-photo" role="img" aria-label="Close-up photo of a cheese and topping pizza"></div>

  <div class="brand-mark">
    <span class="dot" aria-hidden="true"></span>
    <span class="name">Rosalie and Matteo</span>
    <span class="place">ASHFORD, NC<br>555.310.4821</span>
  </div>

  <section class="contact-panel">
    <p class="street">2417 HARBORLINE ROAD ASHFORD, NC 28990</p>
    <p class="phone">(555) 310-4821</p>
    <p class="web">www.rosalieslicehouse.com</p>
  </section>

  <section class="specials" role="img" aria-label="Faded pizza photo behind the weekly specials list">
    <p class="special col-a" style="top:12px">Daily Lunch Special<br>2 Slices + Drink $4.95</p>
    <p class="special col-a" style="top:100px"><span class="day">Monday</span>Buy 1 Medium Pizza<br>Get 1 Free<br>$1 Domestic Beers</p>
    <p class="special col-a" style="top:221px"><span class="day">Tuesday</span>Medium Pizza $7.95<br>50 cent wings<br>$1.50 Drafts</p>
    <p class="special col-a" style="top:340px"><span class="day">Wednesday</span>Classic Burger + Beer $5.95<br>$2.50 Ember Whisky Shots</p>

    <p class="special col-b" style="top:12px"><span class="day">Thursday</span>$1 Slice Night<br>$2.50 Craft Beers</p>
    <p class="special col-b" style="top:117px"><span class="day">Friday</span>2 Medium Pizzas $15.95<br>$2 Glasses of Wine</p>
    <p class="special col-b" style="top:222px"><span class="day">Saturday</span>1/2 Price Salads<br>$3 Vodka Drinks<br>$2.50 Copperline Amber</p>
    <p class="special col-b" style="top:371px"><span class="day">Sunday</span>Large Pizza $9.95<br>$3 Bloody Mary's &amp; Mimosa's</p>
  </section>

  <div class="footer-photo" role="img" aria-label="Wooden table texture"></div>

  <span class="mail-label postage-area">Postage Area</span>
  <span class="mail-label address-area">Address Area</span>
  <span class="mail-label barcode-area">Barcode Area</span>
</main>
</body>
</html>
```